Brightfield Chiropractic Business Cards

Business cards with new logo design. Will upload copy of current card. We like the layout, but we need a new logo. Family, husband holding up baby toward sky, mom and other child standing next to him. We will probably want to include a catch phrase with logo. TBD

```html
<!DOCTYPE html>
<html lang="en">
<head>
<meta charset="utf-8">
<title>Brightfield Chiropractic – Business Cards</title>
<link href="https://fonts.googleapis.com/css2?family=Montserrat:wght@500;600;700&display=swap" rel="stylesheet">
<style>
  :root {
    --navy: #1c2b55;
    --red: #e63b48;
    --red-deep: #dc2f3d;
    --paper: #f2f3f5;
    --panel: #ffffff;
    --stage-top: #0b1633;
    --stage-bottom: #050b1a;
    --map-tone: #eceef2;
  }
  * { box-sizing: border-box; margin: 0; padding: 0; }
  html, body {
    width: 783px; height: 1200px; overflow: hidden;
  }
  body {
    background: linear-gradient(180deg, var(--stage-top), var(--stage-bottom));
    font-family: "Montserrat", sans-serif;
    color: var(--navy);
    position: relative;
  }
  .card {
    position: absolute;
    top: 304px;
    width: 340px;
    height: 592px;
    border-radius: 22px;
    box-shadow: 0 6px 14px rgba(0,0,0,.45);
    text-align: center;
    overflow: hidden;
  }
  .card--front { left: 36px; background: var(--paper); }
  .card--back { left: 407px; background: linear-gradient(180deg, var(--red-deep), var(--red)); }

  .card > * { position: absolute; left: 0; right: 0; }

  .brand-circle {
    left: 85px; right: auto;
    top: 50px;
    width: 170px; height: 170px;
    border: 3px solid var(--navy);
    border-radius: 50%;
  }
  .brand-name {
    top: 230px;
    font-weight: 700;
    font-size: 27px;
    line-height: 30px;
    letter-spacing: .5px;
    color: var(--navy);
  }
  .doctor-name { top: 318px; font-weight: 700; font-size: 17.5px; letter-spacing: .6px; }
  .doctor-title { top: 340px; font-weight: 600; font-size: 14px; letter-spacing: .8px; }
  .divider {
    left: 161px; right: auto;
    width: 18px; height: 3px;
    background: var(--navy);
  }
  .divider--mid { top: 376px; }
  .divider--end { top: 520px; }
  .phone { top: 399px; font-weight: 500; font-size: 15px; letter-spacing: .6px; }
  .website { top: 431px; font-weight: 500; font-size: 15px; letter-spacing: .3px; }
  .website b { font-weight: 700; }
  .address { top: 463px; font-weight: 500; font-size: 13px; line-height: 18px; letter-spacing: .2px; }

  .map-panel {
    left: 21px; right: 21px;
    top: 29px; height: 315px;
    border-radius: 14px;
    background: var(--panel);
  }
  .map-area {
    position: absolute;
    inset: 12px;
    border-radius: 8px;
    background: var(--map-tone);
  }
  .back-name { top: 386px; font-weight: 600; font-size: 17.5px; letter-spacing: .5px; }
  .back-address { top: 418px; font-weight: 500; font-size: 14px; line-height: 21px; }
  .back-tel { top: 468px; font-weight: 500; font-size: 14.5px; letter-spacing: .4px; }
  .back-fax { top: 496px; font-weight: 500; font-size: 14.5px; letter-spacing: .4px; }
  .card--back .divider--end { top: 532px; }
</style>
</head>
<body>
  <section class="card card--front">
    <div class="brand-circle"></div>
    <p class="brand-name">BRIGHTFIELD<br>CHIROPRACTIC</p>
    <p class="doctor-name">DR. DANIEL R. ASHFORD</p>
    <p class="doctor-title">CHIROPRACTIC PHYSICIAN</p>
    <div class="divider divider--mid"></div>
    <p class="phone">503-555-0148</p>
    <p class="website">www.<b>AshfordChiropractic</b>.com</p>
    <p class="address">4820 SE Meadow Crest Dr.<br>Fairview Hills, Oregon 97000</p>
    <div class="divider divider--end"></div>
  </section>

  <section class="card card--back">
    <div class="map-panel">
      <div class="map-area" role="img" aria-label="Street map showing the clinic location between nearby roads and landmarks"></div>
    </div>
    <p class="back-name">BRIGHTFIELD CHIROPRACTIC</p>
    <p class="back-address">4820 SE Meadow Crest Dr.<br>Fairview Hills, Oregon 97000</p>
    <p class="back-tel">Tel.503-555-0148</p>
    <p class="back-fax">Fax.503-555-0172</p>
    <div class="divider divider--end"></div>
  </section>
</body>
</html>
```